Expedition Cruise Sales Website for the Polar Regions (Antarctica & Arctic)

This will be a website for selling cruises.
This site should have a homepage, a ship page, destinations, and itineraries.
I have created a file specifying each page, and it is attached.
Pages:
1. Home
2. Cruise Lines
- 2.1 Ships
3. Destinations
- 3.1 Region - 3.2 Country - 3.3 City
4. Itineraries
- 4.1 Itinerary
5. Blog / Travel Tips 6. About Us
7. Contact
Please take a look on the attached pdf
Target Market(s)
Expedition Travelers
Coding
Coded - Design and coding required
Number of Pages Required
5+ page

```html
<!DOCTYPE html>
<html lang="en">
<head>
<meta charset="utf-8">
<title>Polarvia – Eastern Caribbean Ship</title>
<link href="https://fonts.googleapis.com/css2?family=Inter:wght@400;500;600;700;800&display=swap" rel="stylesheet">
<style>
:root{
  --navy:#0e1a2c;
  --navy-2:#16263d;
  --blue:#3a78c3;
  --blue-dark:#2a5f9f;
  --band:#dde9f5;
  --chip:#dfeaf7;
  --ink:#1b2433;
  --muted:#6b7686;
  --line:#e3e8ef;
  --placeholder:#e4e9ef;
  --white:#fff;
}
*{box-sizing:border-box;margin:0;padding:0}
html,body{width:1200px;height:3888px;overflow:hidden}
body{font-family:"Inter",Arial,sans-serif;color:var(--ink);background:var(--white);position:relative}
.fill{display:block}

/* header */
.hero{height:292px;position:relative;background:linear-gradient(180deg,#1c3550 0%,#3c6688 55%,#8fb2c9 100%);color:#fff}
.nav{position:absolute;top:30px;left:60px;right:60px;display:flex;align-items:center;justify-content:space-between}
.brand{font-size:26px;font-weight:800;color:#fff;display:flex;align-items:center;gap:10px}
.brand i{width:14px;height:14px;background:#fff;border-radius:50%;display:block}
.menu{display:flex;gap:30px;font-size:12px;font-weight:500}
.nav-right{display:flex;align-items:center;gap:22px;font-size:12px;font-weight:600}
.btn{display:inline-block;background:var(--blue);color:#fff;font-size:12px;font-weight:600;padding:10px 20px;border-radius:4px}
.hero h1{position:absolute;top:128px;width:100%;text-align:center;font-size:44px;font-weight:800}

.section-title{text-align:center;font-size:22px;font-weight:700;color:var(--ink)}

/* intro */
.intro{padding-top:92px}
.tabs{display:flex;justify-content:center;gap:10px;margin-top:28px}
.tabs span{background:var(--chip);color:var(--blue-dark);font-size:11px;font-weight:500;padding:7px 14px;border-radius:3px}
.intro p{width:860px;margin:22px auto 0;text-align:center;font-size:11px;line-height:17px;color:var(--muted)}
.gallery{display:grid;grid-template-columns:530px 260px 260px;grid-template-rows:196px 196px;gap:8px;width:1074px;margin:28px auto 0}
.gallery .big{grid-row:1/3}
.gallery div{border-radius:2px}

/* stats */
.tech{margin-top:70px}
.stats{width:1080px;margin:28px auto 0;border:1px solid var(--line);border-radius:6px;display:flex;height:122px;align-items:center}
.stat{flex:1;text-align:center;border-right:1px solid var(--line)}
.stat:last-child{border-right:0}
.stat small{display:block;font-size:11px;color:var(--muted)}
.stat b{display:block;font-size:24px;font-weight:600;margin-top:6px}

/* amenities */
.amenities{position:relative;margin-top:22px;height:300px}
.amenities .band{position:absolute;left:120px;right:120px;top:0;height:170px;background:var(--band)}
.amenities .section-title{position:relative;padding-top:56px}
.amenity-row{position:absolute;top:98px;left:0;right:0;display:flex;gap:6px}
.amenity{flex:1;height:196px;position:relative}
.amenity span{position:absolute;left:0;right:0;bottom:20px;text-align:center;color:#fff;font-size:13px;font-weight:600}

/* cabins */
.cabins{margin-top:50px}
.cabin-row{display:flex;gap:20px;width:1080px;margin:26px auto 0}
.cabin{flex:1;border:1px solid var(--line);border-radius:4px;overflow:hidden}
.cabin .fill{height:160px}
.cabin h3{font-size:14px;font-weight:600;margin:14px 14px 6px}
.cabin p{font-size:10px;line-height:15px;color:var(--muted);margin:0 14px 16px}

/* deckplan */
.deck{position:relative;margin-top:38px;height:640px}
.deck .band{position:absolute;left:120px;right:120px;top:0;height:350px;background:var(--band)}
.deck .section-title{position:relative;padding-top:54px}
.deck-panel{position:absolute;top:96px;left:180px;width:840px;height:500px;background:#fff;border-radius:6px;box-shadow:0 4px 20px rgba(20,40,70,.1);padding:24px}
.deck-head{display:flex;justify-content:space-between;align-items:center}
.deck-head h3{font-size:18px;font-weight:500}
.deck-select{display:flex;gap:10px;font-size:10px;color:var(--muted);align-items:center}
.deck-select span{border:1px solid var(--line);padding:6px 12px;border-radius:3px;color:var(--ink)}
.cat-list{position:absolute;left:24px;top:74px;width:300px}
.cat{display:flex;justify-content:space-between;font-size:10.5px;font-weight:600;padding:9px 0;border-bottom:1px solid var(--line)}
.cat em{font-style:normal;color:var(--muted)}
.cab-nums{display:flex;gap:6px;padding:8px 0}
.cab-nums span{font-size:9px;border:1px solid var(--line);padding:4px 7px;border-radius:2px;color:var(--muted)}
.cab-nums span.on{background:var(--blue);color:#fff;border-color:var(--blue)}
.deck-map{position:absolute;left:400px;top:80px;width:380px;height:390px;background:var(--placeholder);border-radius:4px}

/* departures */
.dep-row{display:flex;gap:20px;justify-content:center;margin-top:26px}
.dep{width:262px;border:1px solid var(--line);border-radius:4px;overflow:hidden;padding-bottom:16px}
.dep .fill{height:150px}
.dep .tag{display:inline-block;margin:12px 12px 0;font-size:9px;background:var(--navy);color:#fff;padding:3px 7px;border-radius:2px}
.dep .tag + small{font-size:9px;color:var(--muted);margin-left:4px}
.dep h3{font-size:12px;font-weight:600;margin:10px 12px 8px}
.dep .meta{display:flex;align-items:center;gap:6px;font-size:9px;color:var(--muted);margin:5px 12px}
.dep .meta i{width:12px;height:12px;border-radius:50%;background:var(--chip);display:block}
.dep .btn{margin:12px 12px 0;font-size:9px;padding:7px 12px}
.dots{display:flex;justify-content:center;gap:6px;margin-top:28px}
.dots i{width:6px;height:6px;border-radius:50%;background:#9aa4b2;display:block}
.dots i:first-child{background:var(--navy)}

/* newsletter */
.newsletter{position:absolute;top:2975px;left:0;width:1200px;height:410px;background:var(--blue);color:#fff}
.newsletter h2{position:absolute;left:100px;top:100px;font-size:38px;font-weight:400;line-height:46px}
.newsletter h2 b{font-weight:700}
.newsletter p{position:absolute;left:100px;top:205px;width:360px;font-size:10px;line-height:15px;color:#e2ecf8}
.form{position:absolute;left:100px;top:255px;width:360px;display:grid;grid-template-columns:1fr 1fr;gap:10px}
.form span{background:#fff;color:var(--muted);font-size:9px;padding:9px 10px;border-radius:2px}
.form .submit{grid-column:1;width:90px;background:var(--navy);color:#fff;text-align:center;font-weight:600}
.news-ship{position:absolute;top:2955px;left:916px;width:186px;height:488px}

/* footer */
.footer{position:absolute;top:3440px;left:0;width:1200px;height:448px;background:linear-gradient(180deg,#1a2a40,var(--navy));color:#c8d2df}
.footer .brand{position:absolute;left:100px;top:90px}
.footer .about{position:absolute;left:100px;top:140px;width:330px;font-size:10px;line-height:16px}
.col{position:absolute;top:86px;font-size:10px;line-height:22px}
.col h4{color:#fff;font-size:13px;font-weight:600;margin-bottom:8px}
.col-contact{left:590px}
.col-links{left:870px}
.col-links ul{list-style:none;display:inline-block;vertical-align:top;width:120px}
.socials{display:flex;gap:8px;margin-top:8px}
.socials i{width:22px;height:22px;border-radius:50%;border:1px solid #6c7d93;display:block}
.row-ic{display:flex;align-items:center;gap:8px}
.copy{position:absolute;left:100px;bottom:34px;font-size:9px;color:#8190a4}
.to-top{position:absolute;right:80px;bottom:34px}
.chat{position:absolute;top:3310px;left:1010px;display:flex;align-items:center;gap:6px}
.chat span{background:#fff;color:var(--ink);font-size:9px;padding:6px 9px;border-radius:4px;box-shadow:0 2px 8px rgba(0,0,0,.15);line-height:12px}
.chat i{width:34px;height:34px;border-radius:50%;background:#37c25b;display:block}
</style>
</head>
<body>

<header class="hero">
  <div class="fill" role="img" aria-label="Cruise ship sailing among icebergs" style="position:absolute;inset:0;background:linear-gradient(180deg,rgba(18,36,58,.55),rgba(18,36,58,.1))"></div>
  <nav class="nav">
    <div class="brand"><i></i>Polarvia</div>
    <div class="menu"><span>Cruise Lines</span><span>Destinations</span><span>Itineraries</span><span>Blog</span><span>About Us</span><span>Contact</span></div>
    <div class="nav-right">
      <span>&#9742; +1 (555) 014-2280</span>
      <span class="btn">Book Now</span>
    </div>
  </nav>
  <h1>Eastern Caribbean Ship</h1>
</header>

<section class="intro">
  <h2 class="section-title">Eastern Caribbean Ship</h2>
  <div class="tabs"><span>Ship Details</span><span>Amenities</span><span>Cabins</span><span>Deck Plans</span><span>Key Specifications</span><span>Available Departures</span></div>
  <p>Set sail on this big, vibrant modern comfort classic vessel with spacious staterooms, multiple pools, relaxed spa, a fitness centre and live entertainment. Every deck is designed for discovery, with open views of turquoise waters and sunny ports along the Eastern Caribbean route.</p>
  <div class="gallery">
    <div class="big fill" role="img" aria-label="Large cruise ship at sea at sunset" style="background:linear-gradient(160deg,#e9b98a 0%,#5d7d9c 45%,#1f4569 100%)"></div>
    <div class="fill" role="img" aria-label="Pool deck with sun loungers" style="background:linear-gradient(160deg,#7cc3de,#2e7fb0)"></div>
    <div class="fill" role="img" aria-label="Bright cabin interior" style="background:linear-gradient(160deg,#eef0f1,#b9c3cc)"></div>
    <div class="fill" role="img" aria-label="Restaurant dining room" style="background:linear-gradient(160deg,#d9a86a,#7d5a36)"></div>
    <div class="fill" role="img" aria-label="Glass observation lounge" style="background:linear-gradient(160deg,#d6e3ee,#8ea7bd)"></div>
  </div>
</section>

<section class="tech">
  <h2 class="section-title">Technical Details</h2>
  <div class="stats">
    <div class="stat"><small>Built</small><b>306 M</b></div>
    <div class="stat"><small>Passenger Capacity</small><b>5,690</b></div>
    <div class="stat"><small>Cabins</small><b>14 Cabins</b></div>
    <div class="stat"><small>Crew</small><b>1,367</b></div>
    <div class="stat"><small>Launch Year</small><b>2011</b></div>
  </div>
</section>

<section class="amenities">
  <div class="band"></div>
  <h2 class="section-title">Amenities</h2>
  <div class="amenity-row">
    <div class="amenity fill" role="img" aria-label="Ship restaurant" style="background:linear-gradient(180deg,#8a6a4c,#2d241c)"><span>Restaurants</span></div>
    <div class="amenity fill" role="img" aria-label="Kids and teens play room" style="background:linear-gradient(180deg,#4a5fa8,#1b2243)"><span>Kids &amp; Teens Room</span></div>
    <div class="amenity fill" role="img" aria-label="Outdoor pools" style="background:linear-gradient(180deg,#7fb8d6,#2b5877)"><span>Pools</span></div>
    <div class="amenity fill" role="img" aria-label="Spa treatment room" style="background:linear-gradient(180deg,#c79a78,#4a3326)"><span>Spa</span></div>
    <div class="amenity fill" role="img" aria-label="Sports deck" style="background:linear-gradient(180deg,#6fa4c9,#284a66)"><span>Sports</span></div>
    <div class="amenity fill" role="img" aria-label="Cocktail bar" style="background:linear-gradient(180deg,#a07a5a,#2c1f16)"><span>Bars</span></div>
  </div>
</section>

<section class="cabins">
  <h2 class="section-title">Types of Cabins</h2>
  <div class="cabin-row">
    <div class="cabin"><div class="fill" role="img" aria-label="Interior cabin" style="background:linear-gradient(160deg,#b59a80,#6d5845)"></div><h3>Interior</h3><p>Cosy and practical rooms with soft lighting, comfortable beds and smart storage for the trip.</p></div>
    <div class="cabin"><div class="fill" role="img" aria-label="Ocean view cabin" style="background:linear-gradient(160deg,#e6ecef,#9fb3c3)"></div><h3>Ocean View</h3><p>Bright rooms with a large window so you can watch the sea from morning to evening.</p></div>
    <div class="cabin"><div class="fill" role="img" aria-label="Balcony cabin" style="background:linear-gradient(160deg,#cfe0ec,#6f94b3)"></div><h3>Balcony</h3><p>Private balcony with seating, fresh sea air and wide views of every port of call.</p></div>
    <div class="cabin"><div class="fill" role="img" aria-label="Suite with lounge" style="background:linear-gradient(160deg,#d8c3a6,#7e6a54)"></div><h3>Suite</h3><p>Spacious suites with a lounge area, premium service and extra comforts on board.</p></div>
  </div>
</section>

<section class="deck">
  <div class="band"></div>
  <h2 class="section-title">Deckplan</h2>
  <div class="deck-panel">
    <div class="deck-head">
      <h3>Cabin Categories</h3>
      <div class="deck-select">Select Deck <span>15 Deck &#9662;</span></div>
    </div>
    <div class="cat-list">
      <div class="cat">Inside <em>&#8964;</em></div>
      <div class="cat">Inside Comfort <em>&#8964;</em></div>
      <div class="cat" style="border-bottom:0">Oceanside <em>&#8963;</em></div>
      <div class="cab-nums"><span class="on">8110</span><span>8112</span><span>8114</span><span>8116</span></div>
      <div class="cab-nums" style="border-bottom:1px solid var(--line)"><span class="on">8120</span><span>8122</span><span>8124</span><span>8126</span></div>
      <div class="cat">Oceanside Comfort <em>&#8964;</em></div>
      <div class="cat">Wellness Incl. <em>&#8964;</em></div>
      <div class="cat">Balcony <em>&#8964;</em></div>
      <div class="cat">Balcony Comfort <em>&#8964;</em></div>
      <div class="cat">Junior Suite W/ Balcony <em>&#8964;</em></div>
      <div class="cat">Suite W/ Balcony <em>&#8964;</em></div>
    </div>
    <div class="deck-map fill" role="img" aria-label="Deck plan drawing of deck 15 with cabin layout"></div>
  </div>
</section>

<section class="departures">
  <h2 class="section-title">Upcoming Departures</h2>
  <div class="dep-row">
    <div class="dep"><div class="fill" role="img" aria-label="Cruise ship in a tropical port" style="background:linear-gradient(160deg,#9cc7e0,#2f6a93)"></div><span class="tag">7 Nights</span><small>10/04/2025 – 17/04/2025</small><h3>Mexico with Aurora of the Waves</h3><div class="meta"><i></i>Galveston (TX), USA</div><div class="meta"><i></i>Costa Maya, Mexico</div><span class="btn">More Details</span></div>
    <div class="dep"><div class="fill" role="img" aria-label="Cruise ship in a tropical port" style="background:linear-gradient(160deg,#9cc7e0,#2f6a93)"></div><span class="tag">7 Nights</span><small>10/04/2025 – 17/04/2025</small><h3>Mexico with Aurora of the Waves</h3><div class="meta"><i></i>Galveston (TX), USA</div><div class="meta"><i></i>Costa Maya, Mexico</div><span class="btn">More Details</span></div>
    <div class="dep"><div class="fill" role="img" aria-label="Cruise ship in a tropical port" style="background:linear-gradient(160deg,#9cc7e0,#2f6a93)"></div><span class="tag">7 Nights</span><small>10/04/2025 – 17/04/2025</small><h3>Mexico with Aurora of the Waves</h3><div class="meta"><i></i>Galveston (TX), USA</div><div class="meta"><i></i>Costa Maya, Mexico</div><span class="btn">More Details</span></div>
  </div>
  <div class="dots"><i></i><i></i><i></i><i></i></div>
</section>

<section class="newsletter">
  <h2>Get cruise deals <b>directly</b><br><b>in your inbox</b></h2>
  <p>Subscribe now and we will let you know about new routes, seasonal offers and polar sailings.</p>
  <div class="form"><span>First Name</span><span>Last Name</span><span>Email</span><span>Phone Number</span><span class="submit">Submit</span></div>
</section>
<div class="news-ship fill" role="img" aria-label="Expedition ship among snowy mountains" style="background:linear-gradient(180deg,#dfe8ef 0%,#b8c9d6 45%,#3f6686 75%,#1d3a55 100%)"></div>

<footer class="footer">
  <div class="brand"><i></i>Polarvia</div>
  <p class="about">Polarvia helps travellers find expedition cruises to the polar regions. We compare ships, routes and departures so you can book with confidence and sail further north and south than ever before.</p>
  <div class="col col-contact">
    <h4>Contact Us</h4>
    <div class="row-ic"><svg width="12" height="12" viewBox="0 0 24 24" fill="#c8d2df"><path d="M6.6 10.8a15 15 0 0 0 6.6 6.6l2.2-2.2c.3-.3.7-.4 1-.2 1.1.4 2.3.6 3.6.6.6 0 1 .4 1 1V20c0 .6-.4 1-1 1A17 17 0 0 1 3 4c0-.6.4-1 1-1h3.5c.6 0 1 .4 1 1 0 1.3.2 2.5.6 3.6.1.3 0 .7-.2 1z"/></svg>+1 (555) 014-2280</div>
    <div class="row-ic"><svg width="12" height="12" viewBox="0 0 24 24" fill="none" stroke="#c8d2df" stroke-width="2"><rect x="3" y="5" width="18" height="14" rx="2"/><path d="M3 7l9 6 9-6"/></svg>hello@polarvia-travel.com</div>
    <h4 style="margin-top:22px">Follow us</h4>
    <div class="socials"><i></i><i></i><i></i><i></i></div>
  </div>
  <div class="col col-links">
    <h4>Quick Links</h4>
    <ul><li>Home</li><li>Cruise Lines</li><li>Destinations</li><li>Itineraries</li><li>Blog</li><li>About Us</li><li>Contact</li></ul><ul><li>FAQ</li><li>Privacy Policy</li><li>Terms and Conditions</li><li>Booking Conditions</li></ul>
  </div>
  <div class="copy">© 2025 Polarvia. All Rights Reserved.</div>
  <svg class="to-top" width="14" height="14" viewBox="0 0 24 24" fill="#fff"><path d="M12 4l9 14H3z"/></svg>
</footer>

<div class="chat"><span>Contact us<br><b>24/7</b></span><i></i></div>

</body>
</html>
```